Senior sex novelty store providing a private method for acquiring the products and knowledge

Our business supplies novelty sex products and services, specializing in the 50+ demographic. Products include sex products for individuals and couples. Services include webinars and teleseminars that address various sex and relationship issues. We are dedicated to providing discreet delivery of products and knowledge to people over 50 entering a new phase of life, facing new challenges. Our entire process from site through shipping is kept private to allow our customers the freedom to shop and learn in the privacy of their own home.

Target Market(s)

Seniors over 50 years old

Industry/Entity Type

Store

Number of Pages Required

1 page

Font styles to use
Serif

Requirements
Must have
• place for business description with a private look
Should not have
• anything sleazy

```html
<!DOCTYPE html>
<html lang="en">
<head>
<meta charset="utf-8">
<title>Your Company Name — Private Store</title>
<link href="https://fonts.googleapis.com/css2?family=Cinzel:wght@400;700&family=PT+Sans:wght@400;700&display=swap" rel="stylesheet">
<style>
:root{
  --red:#c8202f;
  --red-dark:#a51724;
  --ink:#2a2a2a;
  --muted:#7a7a7a;
  --dark:#2c2626;
  --darker:#1d1a1a;
  --header:#3a3333;
  --light:#f2f2f2;
  --white:#ffffff;
  --card-img:#e9e4e4;
}
*{box-sizing:border-box;margin:0;padding:0}
html,body{width:1200px;height:4211px;overflow:hidden}
body{position:relative;background:var(--white);font-family:"PT Sans",Arial,sans-serif;color:var(--ink)}
.serif{font-family:"Cinzel",Georgia,serif}

/* hero */
.hero{position:absolute;left:0;top:0;width:1200px;height:800px;
  background:linear-gradient(135deg,#3a3232 0%,#6d5a52 30%,#c9b7a8 60%,#efe6dc 100%)}
.hero-photo{position:absolute;left:0;top:263px;width:1200px;height:537px;
  background:radial-gradient(ellipse at 35% 50%,#b79c8a 0%,#8a6f62 40%,#d7c8bb 75%,#efe7df 100%)}
.topbar{position:absolute;left:0;top:0;width:1200px;height:263px;
  background:linear-gradient(180deg,#2b2525 0%,#3d3535 100%)}
.logo{position:absolute;left:40px;top:62px;display:flex;align-items:center;gap:18px;color:var(--white)}
.logo-mark{width:44px;height:44px;border:2px solid var(--white)}
.logo-name{font-size:34px;letter-spacing:1px}
.account{position:absolute;right:80px;top:66px;font-size:13px;color:#ddd;display:flex;gap:22px;align-items:center}
.account .cart{color:var(--red);display:flex;align-items:center;gap:6px}
.nav{position:absolute;left:0;top:215px;width:1200px;height:48px;display:flex;justify-content:center;gap:0;
  border-top:1px solid rgba(255,255,255,.08)}
.nav a{color:#eee;text-decoration:none;font-size:16px;line-height:48px;padding:0 30px;position:relative;letter-spacing:.5px}
.nav a+a::before{content:"";position:absolute;left:-2px;top:22px;width:4px;height:4px;background:#ddd;border-radius:50%}
.nav a.active{font-weight:700;color:var(--white);border-bottom:2px solid var(--white)}

/* search */
.search{position:absolute;left:0;top:800px;width:1200px;height:78px;background:var(--red);display:flex;align-items:center;padding-left:105px;gap:12px}
.search-label{color:var(--white);font-size:18px;letter-spacing:1px;width:200px}
.field{height:36px;background:var(--white);display:flex;align-items:center;padding-left:12px;font-size:13px;color:#999;gap:8px}
.f1{width:270px}.f2{width:190px}.f3{width:180px}
.search-btn{width:95px;height:36px;background:#4a3f3f;color:#eee;border:0;font-size:13px;margin-left:8px}

/* welcome */
.welcome{position:absolute;left:0;top:878px;width:1200px;height:1404px;
  background:radial-gradient(ellipse at 50% 40%,#4a3e3c 0%,#2e2726 60%,#221d1d 100%)}
.welcome h2{position:absolute;top:96px;width:100%;text-align:center;color:var(--white);font-size:30px;font-weight:400;letter-spacing:1px}
.welcome .intro{position:absolute;top:146px;left:300px;width:600px;text-align:center;color:#ddd;font-size:16px;line-height:22px}
.card{position:absolute;width:320px;height:432px;background:var(--white);text-align:center}
.card-img{height:210px;background:var(--card-img)}
.card h3{font-size:19px;font-weight:400;margin-top:22px;color:var(--ink)}
.card .rule{width:36px;height:2px;background:var(--red);margin:8px auto 0}
.card .price{font-size:24px;font-weight:700;margin-top:16px}
.card p{font-size:12px;color:var(--muted);line-height:16px;width:190px;margin:10px auto 0}
.card .actions{display:flex;justify-content:center;gap:6px;margin-top:16px}
.btn-more{width:100px;height:34px;background:#e4e4e4;font-size:12px;line-height:34px;color:#444}
.btn-cart{width:52px;height:34px;background:var(--red);display:flex;align-items:center;justify-content:center}
.see-more{position:absolute;top:1264px;width:100%;text-align:center;color:#eee;font-size:18px;letter-spacing:3px}

/* news */
.news{position:absolute;left:0;top:2282px;width:1200px;height:526px;background:var(--white)}
.post{position:absolute;top:80px;width:460px}
.post h2{color:var(--red);font-size:26px;font-weight:400}
.post h4{font-size:16px;font-weight:400;margin-top:40px;line-height:21px;color:#333}
.post .date{font-size:13px;color:#999;margin-top:12px}
.post p{font-size:13px;line-height:19px;color:#555;margin-top:18px}
.post .read{display:block;font-size:13px;color:var(--red);margin-top:44px}

/* social + subscribe */
.social{position:absolute;top:2808px;left:0;width:1200px;display:flex;justify-content:center;gap:8px;z-index:2;transform:translateY(-22px)}
.social span{width:42px;height:42px;border-radius:50%}
.subscribe{position:absolute;left:0;top:2808px;width:1200px;height:369px;
  background:linear-gradient(90deg,#4a3d3b 0%,#1f1a1a 35%,#1f1a1a 65%,#4a3d3b 100%);color:var(--white);text-align:center}
.subscribe h3{margin-top:98px;font-size:20px;font-weight:400;letter-spacing:1px}
.subscribe p{font-size:15px;color:#ccc;margin-top:22px}
.sub-form{display:flex;justify-content:center;margin-top:26px}
.sub-form .input{width:705px;height:46px;background:var(--white)}
.sub-form .go{width:90px;height:46px;background:var(--red);font-size:14px;line-height:46px}

/* map */
.map-title{position:absolute;top:3240px;width:100%;text-align:center;font-size:28px;font-weight:400;color:#333}
.map-rule{position:absolute;top:3290px;left:582px;width:36px;height:2px;background:var(--red)}
.map-sub{position:absolute;top:3300px;width:100%;text-align:center;font-size:16px;color:#777}
.map{position:absolute;left:0;top:3398px;width:1200px;height:323px;background:linear-gradient(90deg,#e8e4dc 0%,#d8dbcf 40%,#a9c5d9 55%,#e3e0d8 75%,#c7d7e2 100%)}

/* contact */
.contact{position:absolute;left:0;top:3721px;width:1200px;height:291px;background:var(--white)}
.in{position:absolute;left:315px;width:275px;height:40px;background:var(--light);font-size:12px;color:#aaa;padding:12px 14px}
.msg{position:absolute;left:605px;top:82px;width:285px;height:92px;background:var(--light);font-size:12px;color:#aaa;padding:12px 14px}
.send{position:absolute;left:605px;top:196px;width:285px;height:40px;background:var(--red);color:var(--white);font-size:13px;text-align:center;line-height:40px}

/* footer */
.footer{position:absolute;left:0;top:4012px;width:1200px;height:199px;background:var(--darker);text-align:center;color:var(--white)}
.footer h2{margin-top:50px;font-size:28px;font-weight:400}
.footer .rule{width:36px;height:2px;background:var(--red);margin:10px auto 0}
.footer nav{margin-top:22px;font-size:13px;color:#bbb;display:flex;justify-content:center;gap:26px}
</style>
</head>
<body>

<header>
  <div class="hero" role="img" aria-label="Soft, warm-toned lifestyle photograph of a woman relaxing on light bedding"></div>
  <div class="hero-photo" role="img" aria-label="Hero photograph in soft cream and warm skin tones"></div>
  <div class="topbar">
    <div class="logo"><span class="logo-mark"></span><span class="logo-name serif">YOUR LOGO</span></div>
    <div class="account">
      <span>LOGIN / SIGNUP</span>
      <span class="cart">
        <svg width="16" height="14" viewBox="0 0 16 14"><path d="M1 1h3l2 8h8l2-6H5" fill="none" stroke="#ddd" stroke-width="1.5"/><circle cx="7" cy="12" r="1.3" fill="#ddd"/><circle cx="13" cy="12" r="1.3" fill="#ddd"/></svg>
        0 ITEM(S)
      </span>
    </div>
    <nav class="nav">
      <a class="active">HOMEPAGE</a><a>PRODUCTS</a><a>SERVICES</a><a>SHIPPING</a><a>PAYMENT</a><a>HELP</a><a>CONTACT</a>
    </nav>
  </div>
</header>

<section class="search">
  <span class="search-label">SEARCH PRODUCTS</span>
  <span class="field f1">
    <svg width="12" height="12" viewBox="0 0 12 12"><path d="M2 10l6-6 2 2-6 6H2z" fill="#999"/></svg>
  </span>
  <span class="field f2">
    <svg width="12" height="12" viewBox="0 0 12 12"><rect x="1" y="1" width="10" height="10" fill="none" stroke="#999"/></svg>Categories
  </span>
  <span class="field f3">
    <svg width="10" height="13" viewBox="0 0 10 13"><path d="M5 12C2 8 1 6 1 4.5a4 4 0 018 0C9 6 8 8 5 12z" fill="#999"/></svg>Locations
  </span>
  <button class="search-btn">Search</button>
</section>

<section class="welcome">
  <h2 class="serif">WELCOME TO OUR STORE</h2>
  <p class="intro">Florem ipsum dolor sit amet voluptatem fugit aut illo omnis explicabo ipsa nemo rem ipsam quasi illo dolores ut voluptatem doloremque perspiciatis beatae magni architecto</p>

  <article class="card" style="left:95px;top:263px">
    <div class="card-img" role="img" aria-label="Product photo in pink tones"></div>
    <h3 class="serif">NEW ARRIVALS</h3><div class="rule"></div>
    <div class="price">$ 250,00</div>
    <p>Discreet choices for a new chapter, shipped in plain packaging.</p>
    <div class="actions"><span class="btn-more">LEARN MORE</span><span class="btn-cart"><svg width="18" height="15" viewBox="0 0 16 14"><path d="M1 1h3l2 8h8l2-6H5" fill="none" stroke="#fff" stroke-width="1.6"/><circle cx="7" cy="12" r="1.4" fill="#fff"/><circle cx="13" cy="12" r="1.4" fill="#fff"/></svg></span></div>
  </article>
  <article class="card" style="left:439px;top:263px">
    <div class="card-img" role="img" aria-label="Product photo in bright pink on a blue background" style="background:linear-gradient(135deg,#bfd0e0,#e88bbd)"></div>
    <h3 class="serif">TOP PRODUCTS</h3><div class="rule"></div>
    <div class="price">$ 250,00</div>
    <p>Our most loved items, chosen by customers over fifty.</p>
    <div class="actions"><span class="btn-more">LEARN MORE</span><span class="btn-cart"><svg width="18" height="15" viewBox="0 0 16 14"><path d="M1 1h3l2 8h8l2-6H5" fill="none" stroke="#fff" stroke-width="1.6"/><circle cx="7" cy="12" r="1.4" fill="#fff"/><circle cx="13" cy="12" r="1.4" fill="#fff"/></svg></span></div>
  </article>
  <article class="card" style="left:786px;top:263px">
    <div class="card-img" role="img" aria-label="Product photo in warm peach tones" style="background:radial-gradient(circle at 50% 55%,#e0a070,#e9e4e4 60%)"></div>
    <h3 class="serif">PROMOS</h3><div class="rule"></div>
    <div class="price">$ 250,00</div>
    <p>Seasonal offers with gentle prices and fully private delivery.</p>
    <div class="actions"><span class="btn-more">LEARN MORE</span><span class="btn-cart"><svg width="18" height="15" viewBox="0 0 16 14"><path d="M1 1h3l2 8h8l2-6H5" fill="none" stroke="#fff" stroke-width="1.6"/><circle cx="7" cy="12" r="1.4" fill="#fff"/><circle cx="13" cy="12" r="1.4" fill="#fff"/></svg></span></div>
  </article>

  <article class="card" style="left:95px;top:740px">
    <div class="card-img" role="img" aria-label="Photo of hands in soft skin tones" style="background:linear-gradient(135deg,#f0e4dc,#d9b6a2)"></div>
    <h3 class="serif">FOR INDIVIDUALS</h3><div class="rule"></div>
    <div class="price">$ 250,00</div>
    <p>Personal comfort products selected with care for every body.</p>
    <div class="actions"><span class="btn-more">LEARN MORE</span><span class="btn-cart"><svg width="18" height="15" viewBox="0 0 16 14"><path d="M1 1h3l2 8h8l2-6H5" fill="none" stroke="#fff" stroke-width="1.6"/><circle cx="7" cy="12" r="1.4" fill="#fff"/><circle cx="13" cy="12" r="1.4" fill="#fff"/></svg></span></div>
  </article>
  <article class="card" style="left:439px;top:740px">
    <div class="card-img" role="img" aria-label="Product photo of soft pink accessories" style="background:linear-gradient(135deg,#e6e2ee,#e58fb2)"></div>
    <h3 class="serif">FOR COUPLES</h3><div class="rule"></div>
    <div class="price">$ 250,00</div>
    <p>Shared experiences to rediscover closeness together, delivered with discretion.</p>
    <div class="actions"><span class="btn-more">LEARN MORE</span><span class="btn-cart"><svg width="18" height="15" viewBox="0 0 16 14"><path d="M1 1h3l2 8h8l2-6H5" fill="none" stroke="#fff" stroke-width="1.6"/><circle cx="7" cy="12" r="1.4" fill="#fff"/><circle cx="13" cy="12" r="1.4" fill="#fff"/></svg></span></div>
  </article>
  <article class="card" style="left:786px;top:740px">
    <div class="card-img" role="img" aria-label="Product photo in deep purple tones" style="background:radial-gradient(circle at 50% 55%,#8a3fa8,#e9e4e4 65%)"></div>
    <h3 class="serif">OTHER PRODUCTS</h3><div class="rule"></div>
    <div class="price">$ 250,00</div>
    <p>Books, care essentials and extras for a confident new phase.</p>
    <div class="actions"><span class="btn-more">LEARN MORE</span><span class="btn-cart"><svg width="18" height="15" viewBox="0 0 16 14"><path d="M1 1h3l2 8h8l2-6H5" fill="none" stroke="#fff" stroke-width="1.6"/><circle cx="7" cy="12" r="1.4" fill="#fff"/><circle cx="13" cy="12" r="1.4" fill="#fff"/></svg></span></div>
  </article>

  <div class="see-more serif">SEE MORE PRODUCTS</div>
</section>

<section class="news">
  <article class="post" style="left:95px">
    <h2 class="serif">RECENT NEWS</h2>
    <h4>OMNIS AUT APERIAM AB IPSAM IPSA ODIT AUT APERIAM AUT ASPERNATUR VERITATIS UNDE</h4>
    <div class="date">April 28, 2015</div>
    <p>Our latest webinar series opens next month with gentle, practical sessions on comfort, confidence and closeness after fifty. Join from home, ask questions privately and revisit every recording whenever it suits you. New titles for individuals and couples have also arrived in the store this week, each packed plainly.</p>
    <a class="read">READ MORE</a>
  </article>
  <article class="post" style="left:645px">
    <h2 class="serif">RELATIONSHIP ISSUES</h2>
    <h4>IPSAM IPSA ODIT AUT APERIAM AUT ASPERNATUR VERITATIS UNDE OMNIS AUT APERIAM AB</h4>
    <div class="date">April 28, 2015</div>
    <p>Many couples find that a new stage of life brings new questions about intimacy. Our teleseminars offer calm, respectful guidance from experienced counsellors, with time for anonymous questions. Listen by phone or online, and keep every session entirely between you and your partner, at your own pace.</p>
    <a class="read">READ MORE</a>
  </article>
</section>

<section class="subscribe" role="img" aria-label="Dark, softly lit photograph of a couple at both sides of the band">
  <h3 class="serif">PLEASE SUBSCRIBE</h3>
  <p>Get our newsletter for various sex new release, promo of the month and relationship issues</p>
  <div class="sub-form"><span class="input"></span><span class="go">Subscribe</span></div>
</section>
<div class="social" aria-label="Social links">
  <span style="background:#3b5998"></span><span style="background:#1da1f2"></span><span style="background:#cb2027"></span><span style="background:#dd4b39"></span>
</div>

<h2 class="map-title serif">SEARCH OUR STORE IN MAP</h2>
<div class="map-rule"></div>
<p class="map-sub">Voluptatem doloremque pempi beatae quia ratione ratione beatae quia ratione ratione dolores</p>
<div class="map" role="img" aria-label="City street map showing the store location beside a river"></div>

<section class="contact">
  <div class="in" style="top:82px">Name</div>
  <div class="in" style="top:139px">Email</div>
  <div class="in" style="top:196px">Phone</div>
  <div class="msg">Message</div>
  <div class="send">send message</div>
</section>

<footer class="footer">
  <h2 class="serif">YOUR COMPANY NAME</h2>
  <div class="rule"></div>
  <nav><span>© 2015 All Rights Reserved</span><span>About us</span><span>Privacy policy</span><span>Terms and use</span><span>Countries</span><span>FAQ</span><span>Contact us</span></nav>
</footer>

</body>
</html>
```